Business Card Design

We need a business card design for a new dental practice in Brisbane. I'd like the basic details and logo on one side and appointment schedule on the other side. It is based in CBD office area and would prefer a professional and modern design.
Target Market(s)
20-60 years old office workers and residents with high education levels
Industry/Entity Type
Dental
Contact Information for Business Card
Harbourlight Dental
Dr Marcus Lindqvist
Principal Dentist
07 3194 6627
admin@harbourlightdentistry.example.au
www.harbourlightdentistry.example.au
S27, Level 3, Ferndale North Tower, 318 Gorrick St, Alderwood Heights, QLD 4118

```html
<!DOCTYPE html>
<html lang="en">
<head>
<meta charset="utf-8">
<title>Harbourlight Dental – Business Card</title>
<link href="https://fonts.googleapis.com/css2?family=Open+Sans:wght@400;600&display=swap" rel="stylesheet">
<style>
  :root {
    --backdrop: #3a3634;
    --card: #ffffff;
    --card-shade: #f1f2f4;
    --ink: #1c2433;
    --accent: #4aaee3;
    --accent-deep: #1f6fb2;
    --rule: #1c2433;
  }
  * { box-sizing: border-box; margin: 0; padding: 0; }
  html, body {
    width: 1200px; height: 886px; overflow: hidden;
    background: var(--backdrop);
    font-family: "Open Sans", Arial, sans-serif;
    color: var(--ink);
  }
  .stage { position: relative; width: 1200px; height: 886px; }
  .card {
    position: absolute; top: 283px;
    width: 530px; height: 320px;
    background: linear-gradient(135deg, var(--card) 55%, var(--card-shade));
    overflow: hidden;
  }
  .card--appointment { left: 45px; }
  .card--details { left: 625px; }

  .brand {
    position: absolute; display: flex; align-items: center; gap: 10px;
    font-size: 30px; font-weight: 400; color: var(--ink); letter-spacing: -0.3px;
    white-space: nowrap;
  }
  .brand__dot { width: 22px; height: 22px; border-radius: 50%; background: var(--accent); }

  .card--appointment .brand { top: 48px; left: 130px; }
  .appointment__heading {
    position: absolute; top: 112px; left: 0; width: 100%;
    text-align: center; font-size: 16px;
  }
  .field { position: absolute; display: flex; align-items: flex-end; font-size: 14px; }
  .field__line { flex: 1; border-bottom: 1px solid var(--rule); margin-left: 6px; height: 16px; }
  .field--name { top: 170px; left: 40px; width: 450px; }
  .field--date { top: 225px; left: 40px; width: 210px; }
  .field--time { top: 225px; left: 265px; width: 225px; }

  .card--details .brand { top: 50px; left: 40px; }
  .details__rule {
    position: absolute; top: 108px; left: 40px; width: 300px;
    border-top: 1px solid var(--rule);
  }
  .person {
    position: absolute; right: 30px; top: 124px;
    border-bottom: 1px solid var(--rule); padding: 0 30px 4px 0;
    white-space: nowrap;
  }
  .person__name { font-size: 21px; line-height: 1.3; }
  .person__role { font-size: 16px; line-height: 1.3; color: var(--accent); }
  .contact { position: absolute; left: 40px; top: 196px; font-size: 13.5px; line-height: 1.45; }
  .contact__row { display: flex; gap: 12px; margin-bottom: 8px; white-space: nowrap; }
  .contact__row svg { flex: none; margin-top: 2px; }
  .details__band {
    position: absolute; left: 0; bottom: 0; width: 100%; height: 26px;
    background: var(--accent);
  }
</style>
</head>
<body>
<main class="stage">
  <section class="card card--appointment" aria-label="Appointment side">
    <div class="brand"><span class="brand__dot"></span>Harbourlight Dental</div>
    <p class="appointment__heading">Your Next Appointment Is:</p>
    <div class="field field--name">Name:<span class="field__line"></span></div>
    <div class="field field--date">Date:<span class="field__line"></span></div>
    <div class="field field--time">Time:<span class="field__line"></span></div>
  </section>

  <section class="card card--details" aria-label="Contact side">
    <div class="brand"><span class="brand__dot"></span>Harbourlight Dental</div>
    <div class="details__rule"></div>
    <div class="person">
      <p class="person__name">Dr Marcus Lindqvist</p>
      <p class="person__role">Principal Dentist</p>
    </div>
    <div class="contact">
      <div class="contact__row">
        <svg width="14" height="14" viewBox="0 0 24 24" aria-hidden="true"><path fill="#1f6fb2" d="M6.6 10.8a15.1 15.1 0 0 0 6.6 6.6l2.2-2.2c.3-.3.7-.4 1-.2 1.1.4 2.3.6 3.6.6.6 0 1 .4 1 1V20c0 .6-.4 1-1 1A17 17 0 0 1 3 4c0-.6.4-1 1-1h3.5c.6 0 1 .4 1 1 0 1.3.2 2.5.6 3.6.1.3 0 .7-.2 1z"/></svg>
        <span>07 3194 6627</span>
      </div>
      <div class="contact__row">
        <svg width="14" height="14" viewBox="0 0 24 24" aria-hidden="true"><path fill="#1f6fb2" d="M12 2a7 7 0 0 0-7 7c0 5.3 7 13 7 13s7-7.7 7-13a7 7 0 0 0-7-7zm0 9.5A2.5 2.5 0 1 1 12 6.5a2.5 2.5 0 0 1 0 5z"/></svg>
        <span>S27, Level 3, Ferndale North Tower,<br>318 Gorrick St, Alderwood Heights, QLD 4118</span>
      </div>
    </div>
    <div class="details__band"></div>
  </section>
</main>
</body>
</html>
```